Packaging label for spirit line

We currently have a various line of spirits and are looking to rebrand the label. The bottle would stay the same since there is a lot of stock. An example of the current situation has been attached. The entire collection is to be found on our website: www.velvetparlor.quinmark.be/spirits

These spirits are a product created by our cocktail bar "Velvet Parlor". The name however, would likely change to "Tipplefox" or plural "Tipplefoxes" since we'd like to split those 2 businesses. The series "shaker lineup" would remain the same as it is a complete series mainly invented for mixology.

The current label is fine, but needs that extra spark that makes it stand out on a shelve compared to other spirit bottles. We envision a more funky yet sophisticated branding with perhaps goldtrims for that "exclusive, luxurious" feel and very much like a vintage animal humification vibe (for example: the marigold or fennick's). Preferably a french bulldog as this has been our mascotte since the very beginning of starting this business.

Last but not least, the measurements: max. 90 mm height and max. 260 mm length. The current label is 90x180mm. 260mm means the label goes fully around the bottle.

Industry/Entity Type

Alcoholic Beverages

Font styles to use
Serif
Sans Serif

Requirements
Must have
• The label must have the standard information such as the product name, the alcohol %, the volume ml and room for ean code. The bottle needs to be sealed for shipment, so a little seal to cover the lid is required.
Nice to have
• It would be nice to maintain consistency with for example the same animal but change of background / colors / outfit / etc to clarify the different flavors. A cutout/contour is also preferable for added interest, so that the label is not square.
Should not have
• The label should definitely not be childish or too much. The overal look and feel needs to be professional yet not too serious.

```html
<!DOCTYPE html>
<html lang="en">
<head>
<meta charset="utf-8">
<title>Tipplefoxes – Velvet Parlor label and seal</title>
<link rel="stylesheet" href="https://fonts.googleapis.com/css2?family=Montserrat:wght@700&family=Open+Sans:wght@300;400&family=Pinyon+Script&family=Libre+Baskerville:ital@1&display=swap">
<style>
  :root {
    --bg-left: #dcdcdc;
    --bg-right: #f1f1f1;
    --brand-green: #4f9b34;
    --text-green: #4a8a3a;
    --band-dark: #2f5a25;
    --band-mid: #4a8f35;
    --band-light: #8dbb7b;
    --label-shade: #b3b5a6;
    --label-cream: #f4f3e3;
    --ink: #3d3d3d;
    --line-green: #7aa869;
    --white: #ffffff;
    --art-dark: #4a4a44;
    --art-light: #9a9b90;
  }
  * { margin: 0; padding: 0; box-sizing: border-box; }
  html, body { width: 1200px; height: 853px; overflow: hidden; }
  body {
    background: linear-gradient(90deg, var(--bg-left), var(--bg-right));
    position: relative;
    font-family: "Open Sans", sans-serif;
  }
  .front-label {
    position: absolute;
    left: 462px;
    top: 396px;
    width: 262px;
    height: 281px;
  }
  .closure-seal {
    position: absolute;
    left: 856px;
    top: 352px;
    width: 200px;
    height: 372px;
  }
  svg { display: block; overflow: visible; }
  .arc-series {
    font-family: "Open Sans", sans-serif;
    font-weight: 300;
    font-size: 14px;
    letter-spacing: 5px;
    fill: var(--text-green);
  }
  .brand-name {
    font-family: "Montserrat", sans-serif;
    font-weight: 700;
    font-size: 21px;
    fill: var(--text-green);
  }
  .category {
    font-family: "Open Sans", sans-serif;
    font-weight: 400;
    font-size: 11px;
    letter-spacing: 4.2px;
    fill: var(--ink);
  }
  .volume {
    font-family: "Libre Baskerville", serif;
    font-style: italic;
    font-size: 9.5px;
    fill: var(--text-green);
  }
  .seal-ring-text {
    font-family: "Open Sans", sans-serif;
    font-weight: 400;
    font-size: 11px;
    letter-spacing: 3.4px;
    fill: var(--ink);
  }
  .seal-brand {
    font-family: "Montserrat", sans-serif;
    font-weight: 700;
    font-size: 10px;
    fill: var(--brand-green);
  }
  .seal-script {
    font-family: "Pinyon Script", cursive;
    font-size: 21px;
    fill: var(--white);
  }
  .seal-volume {
    font-family: "Libre Baskerville", serif;
    font-style: italic;
    font-size: 7px;
    fill: var(--white);
  }
  .strip-script {
    font-family: "Pinyon Script", cursive;
    font-size: 34px;
    fill: var(--white);
  }
</style>
</head>
<body>

<div class="front-label">
  <svg width="262" height="281" viewBox="0 0 262 281">
    <defs>
      <linearGradient id="label-paper" x1="0" y1="0" x2="1" y2="0">
        <stop offset="0" stop-color="var(--label-shade)"/>
        <stop offset="0.45" stop-color="#e4e4d2"/>
        <stop offset="1" stop-color="var(--label-cream)"/>
      </linearGradient>
      <linearGradient id="band-fill" x1="0" y1="0" x2="1" y2="0">
        <stop offset="0" stop-color="var(--band-dark)"/>
        <stop offset="0.55" stop-color="var(--band-mid)"/>
        <stop offset="1" stop-color="var(--band-light)"/>
      </linearGradient>
      <linearGradient id="mascot-tone" x1="0" y1="0" x2="0" y2="1">
        <stop offset="0" stop-color="var(--art-light)"/>
        <stop offset="1" stop-color="var(--art-dark)"/>
      </linearGradient>
      <pattern id="scallop" width="7" height="6" patternUnits="userSpaceOnUse">
        <circle cx="3.5" cy="3" r="3.2" fill="url(#band-fill)"/>
      </pattern>
      <path id="series-arc" d="M46,92 A88,88 0 0,1 216,92"/>
    </defs>

    <rect class="label-paper" x="0" y="0" width="262" height="281" fill="url(#label-paper)"/>

    <text class="arc-series" text-anchor="middle">
      <textPath href="#series-arc" startOffset="50%">VELVET PARLOR</textPath>
    </text>

    <rect class="mascot-art" x="62" y="42" width="128" height="118" rx="6"
          fill="url(#mascot-tone)" opacity="0.55"
          role="img" aria-label="Illustration of the bulldog mascot in a dinner jacket and bow tie, raising a glass of wine"/>

    <text class="brand-name" x="131" y="180" text-anchor="middle" textLength="196" lengthAdjust="spacingAndGlyphs">TIPPLEFOXES</text>
    <line class="rule" x1="8" y1="186" x2="254" y2="182" stroke="var(--line-green)" stroke-width="0.8"/>
    <text class="category" x="131" y="204" text-anchor="middle">DISTILLED SPIRIT</text>
    <line class="rule" x1="8" y1="212" x2="254" y2="208" stroke="var(--line-green)" stroke-width="0.8"/>

    <g class="wave-band">
      <rect x="0" y="220" width="262" height="28" fill="url(#band-fill)"/>
      <rect x="0" y="216" width="262" height="6" fill="url(#scallop)"/>
      <rect x="0" y="246" width="262" height="6" fill="url(#scallop)"/>
    </g>

    <text class="volume" x="131" y="270" text-anchor="middle">500 ml 38.0% vol.alc</text>
  </svg>
</div>

<div class="closure-seal">
  <svg width="200" height="372" viewBox="0 0 200 372">
    <defs>
      <clipPath id="lower-half">
        <rect x="0" y="94" width="200" height="100"/>
      </clipPath>
      <path id="ring-top" d="M28.6,64 A76,76 0 0,1 171.4,64"/>
      <path id="ring-bottom" d="M37.7,133.6 A76,76 0 0,0 162.3,133.6"/>
    </defs>

    <rect class="seal-strip" x="48" y="160" width="105" height="212" fill="var(--brand-green)"/>
    <rect class="strip-frame" x="58" y="170" width="85" height="192" fill="none" stroke="var(--ink)" stroke-width="1.4"/>
    <text class="strip-script" transform="translate(112 348) rotate(-90)">Velvet Parlor</text>

    <circle class="seal-ring" cx="100" cy="90" r="89" fill="var(--white)"/>
    <circle class="seal-ring-lower" cx="100" cy="90" r="89" fill="var(--brand-green)" clip-path="url(#lower-half)"/>
    <path class="seal-name-band" d="M37.7,133.6 A76,76 0 0,0 162.3,133.6" fill="none" stroke="var(--white)" stroke-width="20"/>
    <circle class="seal-outline" cx="100" cy="90" r="89" fill="none" stroke="var(--ink)" stroke-width="1.4"/>

    <text class="seal-ring-text" text-anchor="middle" dominant-baseline="middle">
      <textPath href="#ring-top" startOffset="50%">DISTILLED SPIRIT</textPath>
    </text>
    <text class="seal-brand" text-anchor="middle" dominant-baseline="middle">
      <textPath href="#ring-bottom" startOffset="50%">TIPPLEFOXES</textPath>
    </text>

    <circle class="seal-center" cx="100" cy="90" r="63" fill="var(--brand-green)" stroke="var(--white)" stroke-width="2"
            role="img" aria-label="Green field with a faint botanical pattern of leafy sprigs and berries"/>
    <text class="seal-script" x="100" y="96" text-anchor="middle">Velvet Parlor</text>
    <text class="seal-volume" x="100" y="112" text-anchor="middle">500 ml 38.0% vol.alc</text>
  </svg>
</div>

</body>
</html>
```